Website transfer and revamp for consultancy

We are a professional management consultancy and need our current website transferred and modernised from Wix to WordPress with the most efficient SEO updates and blog included. We are open for options of new site set up.

Website must be relatively easy for us to maintain and update ourselves.

Website must also be desktop/mobile/ipad friendly.

www.tellvane-advisory.com

Target Market(s)

General manufacturers, construction, developers, oil and gas

Industry/Entity Type

Management Consulting

Font styles to use
Serif

Colors

Designer to choose colors to be used in the design.

Requirements
Must have
• Must have same bulk content as the existing website as a minimum with the addition of a blog page. We are open to added content.
Nice to have
• Open to designer additions such as "projects completed" and "value created" number generators
Should not have
• DO NOT USE stock photos which are not free for use to use.

```html
<!DOCTYPE html>
<html lang="en">
<head>
<meta charset="utf-8">
<title>Tellvane Advisory — The Contract and Conflict Advisory</title>
<link href="https://fonts.googleapis.com/css2?family=Cinzel:wght@400;700&family=Open+Sans:wght@400;600;700&display=swap" rel="stylesheet">
<style>
:root{
  --navy:#1d3f63;
  --navy-deep:#1b2b57;
  --red:#c1202f;
  --ink:#1f2430;
  --muted:#6b7280;
  --line:#e3e5ea;
  --white:#ffffff;
  --serif:'Cinzel', Georgia, serif;
  --sans:'Open Sans', Arial, sans-serif;
}
*{box-sizing:border-box;margin:0;padding:0}
html,body{width:1200px;height:2980px;overflow:hidden}
body{position:relative;background:var(--white);font-family:var(--sans);color:var(--ink)}
a{color:inherit;text-decoration:none}
ul{list-style:none}

/* Header */
.site-header{position:absolute;top:0;left:0;width:1200px;height:130px;background:var(--white)}
.brand{position:absolute;left:100px;top:24px;display:flex;align-items:center;gap:12px}
.brand-dot{width:30px;height:30px;border-radius:50%;background:var(--red);flex:none}
.brand-name{font-family:var(--serif);font-weight:700;font-size:26px;color:var(--navy);line-height:1;white-space:nowrap}
.brand-tag{position:absolute;left:100px;top:92px;font-family:var(--serif);font-size:9.5px;color:var(--navy);letter-spacing:.3px}
.header-actions{position:absolute;right:100px;top:24px;display:flex;gap:10px}
.btn-pill{height:42px;border-radius:21px;padding:0 28px;display:flex;align-items:center;font-size:13px;font-weight:700;color:var(--white);text-transform:uppercase}
.btn-pill.navy{background:var(--navy)}
.btn-pill.red{background:var(--red)}
.main-nav{position:absolute;right:100px;top:92px;display:flex;gap:34px;align-items:center;font-family:var(--serif);font-size:13px;color:var(--ink)}
.main-nav .active{font-weight:700;color:var(--navy);position:relative}
.main-nav .active::before{content:"";position:absolute;left:50%;top:-22px;width:18px;height:14px;margin-left:-9px;border-radius:50%;background:var(--red)}

/* Hero */
.hero{position:absolute;top:130px;left:0;width:1200px;height:641px;overflow:hidden}
.hero-photo{position:absolute;inset:0;background:linear-gradient(180deg,#5d6470 0%,#3f4654 45%,#2a303c 100%)}
.hero-shade{position:absolute;inset:0;background:rgba(20,26,38,.35)}
.hero-curve{position:absolute;left:0;top:0}
.hero-title{position:absolute;top:230px;width:100%;text-align:center;font-family:var(--serif);font-size:64px;color:var(--white);letter-spacing:2px}
.hero-sub{position:absolute;top:320px;width:100%;text-align:center;font-family:var(--serif);font-size:22px;color:var(--white);letter-spacing:1px}
.hero-regions{position:absolute;top:368px;width:100%;display:flex;justify-content:center;gap:22px;font-family:var(--serif);font-size:13px;color:var(--white)}
.hero-regions span+span::before{content:"•";margin-right:22px}
.hero-arrow{position:absolute;top:258px}
.hero-arrow.left{left:14px}.hero-arrow.right{right:14px}
.commit-badge{position:absolute;left:530px;top:410px;width:140px;height:140px;border-radius:50%;border:3px solid var(--white);background:var(--red);display:flex;align-items:center;justify-content:center}
.commit-badge span{width:116px;height:116px;border-radius:50%;background:var(--white);display:flex;align-items:center;justify-content:center;font-size:38px;font-weight:700;color:var(--red)}
.commit-badge sup{font-size:16px;margin-left:2px}
.commit-text{position:absolute;top:568px;width:100%;text-align:center;font-size:14px;font-weight:600;color:var(--white);line-height:22px}

/* Sectors */
.welcome{position:absolute;top:771px;left:0;width:1200px;height:495px}
.section-title{font-family:var(--serif);font-size:32px;color:var(--navy-deep);text-align:center}
.welcome .section-title{margin-top:60px}
.welcome-lead{width:560px;margin:22px auto 0;text-align:center;font-size:14px;line-height:24px;color:var(--muted)}
.sector{position:absolute;top:210px;width:240px;text-align:center}
.sector svg{display:block;margin:0 auto}
.sector p{margin-top:14px;font-size:16px;line-height:24px;color:var(--ink)}

/* Advisory split */
.advisory{position:absolute;top:1266px;left:0;width:1200px;height:447px;display:flex}
.advisory-panel{position:relative;width:600px;height:447px;padding:55px 0 0 100px;color:var(--white)}
.advisory-panel.conflict{background:linear-gradient(135deg,#2a5177 0%,#1d3f63 100%)}
.advisory-panel.contract{background:linear-gradient(135deg,#1e2f60 0%,#1a2752 100%);padding-left:125px}
.advisory-panel h2{font-family:var(--serif);font-weight:400;font-size:32px;letter-spacing:.5px}
.advisory-panel ul{margin-top:22px;width:370px}
.advisory-panel li{position:relative;padding-left:28px;font-size:14px;line-height:22px;margin-bottom:22px}
.advisory-panel li svg{position:absolute;left:0;top:3px}
.btn-outline{position:absolute;left:100px;top:336px;width:132px;height:44px;border:2px solid var(--white);border-radius:22px;display:flex;align-items:center;justify-content:center;font-size:13px;font-weight:700}
.contract .btn-outline{left:125px}
.advisory-mark{position:absolute;left:548px;top:170px;width:104px;height:104px;border-radius:50%;background:var(--white)}

/* Blog */
.blog{position:absolute;top:1713px;left:0;width:1200px;height:628px}
.blog .section-title{margin-top:80px}
.post{position:absolute;top:157px;width:322px}
.post-media{width:322px;height:209px}
.post-media.one{background:linear-gradient(160deg,#cfd6dc,#7f8d99)}
.post-media.two{background:linear-gradient(160deg,#e8e4df,#a9a6a3)}
.post-media.three{background:linear-gradient(160deg,#dfe5d2,#b8a58a)}
.post h3{margin-top:32px;font-size:19px;font-weight:600;color:var(--ink)}
.post-meta{margin-top:10px;display:flex;align-items:center;gap:8px;font-size:12px;color:var(--muted)}
.post-meta .sep{margin:0 4px}
.post-excerpt{margin-top:14px;font-size:12.5px;line-height:22px;color:var(--muted)}
.read-more{display:block;margin-top:14px;font-size:13px;font-weight:700;color:var(--red)}

/* Stats */
.stats{position:absolute;top:2341px;left:0;width:1200px;height:262px}
.stats-photo{position:absolute;inset:0;background:linear-gradient(90deg,#4a4d55 0%,#7b6c5e 45%,#c98a45 75%,#e7a24c 100%)}
.stat{position:absolute;top:52px;display:flex;align-items:center}
.stat-ring{width:152px;height:152px;border-radius:50%;border:3px solid var(--white);display:flex;align-items:center;justify-content:center}
.stat-figure{margin-left:28px;color:var(--white)}
.stat-figure strong{display:block;font-size:48px;font-weight:700;line-height:52px}
.stat-figure span{display:block;font-family:var(--serif);font-size:23px;letter-spacing:.5px;margin-top:4px}

/* Footer */
.site-footer{position:absolute;top:2603px;left:0;width:1200px;height:377px;background:var(--white)}
.footer-brand{position:absolute;left:95px;top:100px;width:270px;text-align:center}
.footer-brand .brand-dot{display:block;width:56px;height:56px;margin:0 auto}
.footer-brand .brand-name{display:block;margin-top:22px;font-size:21px}
.footer-brand small{display:block;margin-top:8px;font-family:var(--serif);font-size:10px;color:var(--navy);white-space:nowrap}
.footer-col{position:absolute;top:82px}
.footer-col h4{font-family:var(--serif);font-weight:400;font-size:19px;color:var(--ink);margin-bottom:20px;white-space:nowrap}
.quick-links li{font-size:12px;color:var(--ink);line-height:25px}
.newsletter p{width:250px;font-size:12px;line-height:20px;color:var(--ink)}
.newsletter .field{margin-top:14px;width:255px;border-bottom:1px solid #c9ccd2;padding:6px 0 8px;font-size:11px;color:#9aa0a8}
.newsletter .btn-sub{margin-top:20px;width:106px;height:32px;border-radius:16px;background:var(--red);color:var(--white);font-size:11px;font-weight:700;display:flex;align-items:center;justify-content:center}
.contact li{position:relative;padding-left:34px;font-size:12px;line-height:20px;color:var(--ink);margin-bottom:18px;width:240px}
.contact li svg{position:absolute;left:0;top:3px}
.footer-bottom{position:absolute;left:100px;top:294px;width:1000px;border-top:1px solid var(--line);padding-top:28px;display:flex;justify-content:space-between;align-items:center}
.footer-bottom p{font-size:12px;color:var(--muted)}
.social{display:flex;gap:10px}
.social span{width:26px;height:26px;border-radius:50%;border:1.5px solid var(--red)}
</style>
</head>
<body>

<header class="site-header">
  <div class="brand"><span class="brand-dot"></span><span class="brand-name">Tellvane Advisory</span></div>
  <div class="brand-tag">THE CONTRACT AND CONFLICT ADVISORY</div>
  <div class="header-actions">
    <a class="btn-pill navy" href="#">Arrange a Consultation</a>
    <a class="btn-pill red" href="#">Brochure</a>
  </div>
  <nav class="main-nav">
    <a class="active" href="#">HOME</a>
    <a href="#">ABOUT US</a>
    <a href="#">CONFLICT ADVISORY</a>
    <a href="#">CONTRACT ADVISORY</a>
    <a href="#">BLOG</a>
    <a href="#">CONTACT US</a>
    <svg width="14" height="14" viewBox="0 0 14 14" aria-label="Search"><circle cx="6" cy="6" r="4.5" fill="none" stroke="#1f2430" stroke-width="2"/><line x1="9.3" y1="9.3" x2="13" y2="13" stroke="#1f2430" stroke-width="2"/></svg>
  </nav>
</header>

<section class="hero">
  <div class="hero-photo" role="img" aria-label="Team of consultants meeting around a boardroom table reviewing charts"></div>
  <div class="hero-shade"></div>
  <svg class="hero-curve" width="1200" height="641" viewBox="0 0 1200 641"><path d="M0 424 Q600 516 1200 424 L1200 641 L0 641 Z" fill="#c1202f"/></svg>
  <svg class="hero-arrow left" width="14" height="22" viewBox="0 0 14 22"><polyline points="11,3 3,11 11,19" fill="none" stroke="#fff" stroke-width="2.5"/></svg>
  <svg class="hero-arrow right" width="14" height="22" viewBox="0 0 14 22"><polyline points="3,3 11,11 3,19" fill="none" stroke="#fff" stroke-width="2.5"/></svg>
  <h1 class="hero-title">TELLVANE ADVISORY</h1>
  <p class="hero-sub">THE CONTRACT AND CONFLICT ADVISORY</p>
  <div class="hero-regions"><span>UNITED KINGDOM</span><span>IRELAND</span><span>UNITED ARAB EMIRATES</span></div>
  <div class="commit-badge"><span>100<sup>%</sup></span></div>
  <p class="commit-text">The commitment we give our clients to<br>obtain the highest contract value</p>
</section>

<section class="welcome">
  <h2 class="section-title">Welcome to Tellvane Advisory</h2>
  <p class="welcome-lead">We are an experienced contract and conflict advisory providing global contract performance solutions and conflict manage-ment to:</p>

  <div class="sector" style="left:105px">
    <svg width="150" height="150" viewBox="0 0 150 150">
      <path d="M110 28 A64 64 0 1 0 110 122" fill="none" stroke="#1d3f63" stroke-width="16"/>
      <path d="M102 40 A50 50 0 0 1 102 110" fill="none" stroke="#c1202f" stroke-width="10"/>
      <circle cx="72" cy="75" r="34" fill="#1d3f63"/>
      <circle cx="72" cy="75" r="13" fill="none" stroke="#fff" stroke-width="2.5"/>
      <path d="M66 69 q6 3 4 8 q-4 2 -6 -2 z M76 78 q4 -2 6 2 q-3 4 -6 2 z" fill="#fff"/>
    </svg>
    <p>International development<br>organisations</p>
  </div>
  <div class="sector" style="left:363px">
    <svg width="150" height="150" viewBox="0 0 150 150">
      <path d="M110 28 A64 64 0 1 0 110 122" fill="none" stroke="#1d3f63" stroke-width="16"/>
      <path d="M102 40 A50 50 0 0 1 102 110" fill="none" stroke="#c1202f" stroke-width="10"/>
      <circle cx="72" cy="75" r="34" fill="#1d3f63"/>
      <rect x="63" y="60" width="18" height="30" fill="#fff"/>
      <g fill="#1d3f63"><rect x="66" y="64" width="4" height="4"/><rect x="74" y="64" width="4" height="4"/><rect x="66" y="72" width="4" height="4"/><rect x="74" y="72" width="4" height="4"/><rect x="70" y="82" width="4" height="8"/></g>
    </svg>
    <p>Construction industry</p>
  </div>
  <div class="sector" style="left:621px">
    <svg width="150" height="150" viewBox="0 0 150 150">
      <path d="M110 28 A64 64 0 1 0 110 122" fill="none" stroke="#1d3f63" stroke-width="16"/>
      <path d="M102 40 A50 50 0 0 1 102 110" fill="none" stroke="#c1202f" stroke-width="10"/>
      <circle cx="72" cy="75" r="34" fill="#1d3f63"/>
      <path d="M72 60 C66 70 62 76 62 82 A10 10 0 0 0 82 82 C82 76 78 70 72 60 Z" fill="#fff"/>
    </svg>
    <p>Oil and gas industry</p>
  </div>
  <div class="sector" style="left:879px">
    <svg width="150" height="150" viewBox="0 0 150 150">
      <path d="M110 28 A64 64 0 1 0 110 122" fill="none" stroke="#1d3f63" stroke-width="16"/>
      <path d="M102 40 A50 50 0 0 1 102 110" fill="none" stroke="#c1202f" stroke-width="10"/>
      <circle cx="72" cy="75" r="34" fill="#1d3f63"/>
      <g fill="#fff"><polygon points="72,59 56,67 88,67"/><rect x="58" y="69" width="28" height="2"/><rect x="60" y="73" width="3" height="12"/><rect x="66" y="73" width="3" height="12"/><rect x="75" y="73" width="3" height="12"/><rect x="81" y="73" width="3" height="12"/><rect x="56" y="87" width="32" height="3"/></g>
    </svg>
    <p>Government sectors</p>
  </div>
</section>

<section class="advisory">
  <div class="advisory-panel conflict">
    <h2>CONFLICT ADVISORY</h2>
    <ul>
      <li><svg width="16" height="16" viewBox="0 0 16 16"><circle cx="8" cy="8" r="8" fill="#fff"/><polyline points="4.5,8 7,10.5 11.5,5.5" fill="none" stroke="#1d3f63" stroke-width="2"/></svg>Restoration and Mediation Services</li>
      <li><svg width="16" height="16" viewBox="0 0 16 16"><circle cx="8" cy="8" r="8" fill="#fff"/><polyline points="4.5,8 7,10.5 11.5,5.5" fill="none" stroke="#1d3f63" stroke-width="2"/></svg>Shuttle Diplomacy Services and In Personal Intermediary Services</li>
      <li><svg width="16" height="16" viewBox="0 0 16 16"><circle cx="8" cy="8" r="8" fill="#fff"/><polyline points="4.5,8 7,10.5 11.5,5.5" fill="none" stroke="#1d3f63" stroke-width="2"/></svg>Negotiation Support Services</li>
      <li><svg width="16" height="16" viewBox="0 0 16 16"><circle cx="8" cy="8" r="8" fill="#fff"/><polyline points="4.5,8 7,10.5 11.5,5.5" fill="none" stroke="#1d3f63" stroke-width="2"/></svg>Workplace Mediation Services</li>
    </ul>
    <a class="btn-outline" href="#">READ MORE</a>
  </div>
  <div class="advisory-panel contract">
    <h2>CONTRACT ADVISORY</h2>
    <ul>
      <li><svg width="16" height="16" viewBox="0 0 16 16"><circle cx="8" cy="8" r="8" fill="#fff"/><polyline points="4.5,8 7,10.5 11.5,5.5" fill="none" stroke="#1b2b57" stroke-width="2"/></svg>Contract Troubleshooting</li>
      <li><svg width="16" height="16" viewBox="0 0 16 16"><circle cx="8" cy="8" r="8" fill="#fff"/><polyline points="4.5,8 7,10.5 11.5,5.5" fill="none" stroke="#1b2b57" stroke-width="2"/></svg>Contracts Audit Services and Performance Management</li>
      <li><svg width="16" height="16" viewBox="0 0 16 16"><circle cx="8" cy="8" r="8" fill="#fff"/><polyline points="4.5,8 7,10.5 11.5,5.5" fill="none" stroke="#1b2b57" stroke-width="2"/></svg>Strategic Review &amp; Risk Assessment</li>
      <li><svg width="16" height="16" viewBox="0 0 16 16"><circle cx="8" cy="8" r="8" fill="#fff"/><polyline points="4.5,8 7,10.5 11.5,5.5" fill="none" stroke="#1b2b57" stroke-width="2"/></svg>Contract Fraud Investigation</li>
    </ul>
    <a class="btn-outline" href="#">READ MORE</a>
  </div>
  <div class="advisory-mark"></div>
</section>

<section class="blog">
  <h2 class="section-title">Latest Blog</h2>
  <article class="post" style="left:99px">
    <div class="post-media one" role="img" aria-label="Business people talking in a bright office lobby"></div>
    <h3>Finibus Bonorum et Malorum</h3>
    <div class="post-meta">
      <svg width="12" height="12" viewBox="0 0 12 12"><rect x="1" y="2" width="10" height="9" fill="none" stroke="#c1202f" stroke-width="1.4"/><line x1="1" y1="5" x2="11" y2="5" stroke="#c1202f" stroke-width="1.4"/></svg>25/09/2017<span class="sep">|</span>
      <svg width="12" height="12" viewBox="0 0 12 12"><circle cx="6" cy="4" r="2.6" fill="#1d3f63"/><path d="M1.5 11.5 a4.5 4 0 0 1 9 0 z" fill="#1d3f63"/></svg>Maren
    </div>
    <p class="post-excerpt">Nemo enim ipsam voluptatem quia volupta asperna tur aut odit aut fugit, sed quia conseq.</p>
    <a class="read-more" href="#">READ MORE</a>
  </article>
  <article class="post" style="left:439px">
    <div class="post-media two" role="img" aria-label="Hands reviewing and signing a contract document"></div>
    <h3>Finibus Bonorum et Malorum</h3>
    <div class="post-meta">
      <svg width="12" height="12" viewBox="0 0 12 12"><rect x="1" y="2" width="10" height="9" fill="none" stroke="#c1202f" stroke-width="1.4"/><line x1="1" y1="5" x2="11" y2="5" stroke="#c1202f" stroke-width="1.4"/></svg>25/09/2017<span class="sep">|</span>
      <svg width="12" height="12" viewBox="0 0 12 12"><circle cx="6" cy="4" r="2.6" fill="#1d3f63"/><path d="M1.5 11.5 a4.5 4 0 0 1 9 0 z" fill="#1d3f63"/></svg>Maren
    </div>
    <p class="post-excerpt">Nemo enim ipsam voluptatem quia volupta asperna tur aut odit aut fugit, sed quia conseq.</p>
    <a class="read-more" href="#">READ MORE</a>
  </article>
  <article class="post" style="left:777px">
    <div class="post-media three" role="img" aria-label="Consultants discussing paperwork around a desk"></div>
    <h3>Finibus Bonorum et Malorum</h3>
    <div class="post-meta">
      <svg width="12" height="12" viewBox="0 0 12 12"><rect x="1" y="2" width="10" height="9" fill="none" stroke="#c1202f" stroke-width="1.4"/><line x1="1" y1="5" x2="11" y2="5" stroke="#c1202f" stroke-width="1.4"/></svg>25/09/2017<span class="sep">|</span>
      <svg width="12" height="12" viewBox="0 0 12 12"><circle cx="6" cy="4" r="2.6" fill="#1d3f63"/><path d="M1.5 11.5 a4.5 4 0 0 1 9 0 z" fill="#1d3f63"/></svg>Maren
    </div>
    <p class="post-excerpt">Nemo enim ipsam voluptatem quia volupta asperna tur aut odit aut fugit, sed quia conseq.</p>
    <a class="read-more" href="#">READ MORE</a>
  </article>
</section>

<section class="stats">
  <div class="stats-photo" role="img" aria-label="Close-up of a business handshake in warm light"></div>
  <div class="stat" style="left:100px">
    <div class="stat-ring">
      <svg width="58" height="58" viewBox="0 0 58 58"><g fill="#fff"><circle cx="22" cy="32" r="14"/><circle cx="42" cy="16" r="9"/></g><g stroke="#fff" stroke-width="5"><line x1="22" y1="14" x2="22" y2="50"/><line x1="4" y1="32" x2="40" y2="32"/><line x1="9" y1="19" x2="35" y2="45"/><line x1="35" y1="19" x2="9" y2="45"/><line x1="42" y1="4" x2="42" y2="28"/><line x1="30" y1="16" x2="54" y2="16"/></g><g fill="#7a6b5e"><circle cx="22" cy="32" r="5"/><circle cx="42" cy="16" r="3.5"/></g></svg>
    </div>
    <div class="stat-figure"><strong>125830</strong><span>PROJECTS COMPLETED</span></div>
  </div>
  <div class="stat" style="left:665px">
    <div class="stat-ring">
      <svg width="58" height="58" viewBox="0 0 58 58"><circle cx="29" cy="29" r="26" fill="#fff"/><polyline points="17,30 26,39 42,21" fill="none" stroke="#b07c48" stroke-width="6" stroke-linecap="round" stroke-linejoin="round"/></svg>
    </div>
    <div class="stat-figure"><strong>125830</strong><span>VALUE CREATED</span></div>
  </div>
</section>

<footer class="site-footer">
  <div class="footer-brand">
    <span class="brand-dot"></span>
    <span class="brand-name">Tellvane Advisory</span>
    <small>THE CONTRACT AND CONFLICT ADVISORY</small>
  </div>

  <div class="footer-col quick-links" style="left:401px">
    <h4>Quick Links</h4>
    <ul><li>Home</li><li>About Us</li><li>Conflict Advisory</li><li>Contract Advisory</li><li>Blog</li><li>Contact Us</li></ul>
  </div>

  <div class="footer-col newsletter" style="left:572px">
    <h4>Newsletter Subscription</h4>
    <p>Register your Email Address to get information about us</p>
    <div class="field">Email Address</div>
    <a class="btn-sub" href="#">SUBSCRIBE</a>
  </div>

  <div class="footer-col contact" style="left:876px">
    <h4>Contact Us</h4>
    <ul>
      <li><svg width="12" height="16" viewBox="0 0 12 16"><path d="M6 0 a6 6 0 0 1 6 6 c0 4 -6 10 -6 10 s-6 -6 -6 -10 a6 6 0 0 1 6 -6 z" fill="#c1202f"/><circle cx="6" cy="6" r="2.2" fill="#fff"/></svg>Orrin Works Ltd, 2nd Floor,<br>Halden House, 40-44 Quay Lane,<br>Harbour Quarter, Belfast, BT2 9QX</li>
      <li><svg width="14" height="14" viewBox="0 0 14 14"><path d="M3 0.5 l2.5 3 -1.5 2 a8 8 0 0 0 4.5 4.5 l2 -1.5 3 2.5 -1.5 2.5 C6 13 1 8 0.5 2 z" fill="#c1202f"/></svg>1 800 555 0142</li>
      <li><svg width="14" height="12" viewBox="0 0 14 12"><rect x="0" y="1" width="14" height="10" fill="#c1202f"/><polyline points="0.5,1.5 7,7 13.5,1.5" fill="none" stroke="#fff" stroke-width="1.3"/></svg>mdoyle@tellvane-advisory.com</li>
    </ul>
  </div>

  <div class="footer-bottom">
    <p>Copyrights © 2018, Tellvane-advisory.com. All rights reserved.</p>
    <div class="social"><span></span><span></span><span></span><span></span></div>
  </div>
</footer>

</body>
</html>
```